Brochure Design Project

We need to update our brochure to include new text, photos and additional logos. Looking for something that will catch the eye of tourists. Must be A4 3 fold as this is the type of brochure stands all Visitor Information Centres have.

Previous brochure attached together with logos. Pictures can be access via our pixroa albums http://pixoraweb.vendrel.com/482917305618274039162

Target Market(s)

International visitors visiting Australia normally high income adults but some come with children and can be wealthier retired adults

Industry/Entity Type

Vendrel

Requirements
Must have
• Pictures that feature areas we tour
Nice to have
• Believe some customer comments would be add value to the brochure these can be found on our website at http://bramblewaytours.com.au/testimonials.php

or RoamRater
http://www.roamrater.com.au/Attraction_Review-g381726-d5930471-Reviews-Brambleway_TRUEpath_Day_Tours-Melbourne_Victoria.html

```html
<!DOCTYPE html>
<html lang="en">
<head>
<meta charset="utf-8">
<title>Brambleway TRUEpath Tours – Tri-fold Brochure, Front Side</title>
<link rel="stylesheet" href="https://fonts.googleapis.com/css2?family=PT+Sans:wght@400;700&family=Cinzel:wght@400;700&display=swap">
<style>
  :root {
    --stage: #111111;
    --red: #b3202a;
    --cream: #fbeecb;
    --cream-light: #fff8e6;
    --blue-title: #1f6fb5;
    --text: #2a2a2a;
    --band-orange: #f3a23a;
    --band-blue: #8fd3ef;
    --band-green: #a9cf3a;
    --feature-beige: #c9785c;
    --feature-yellow: #c28a12;
    --feature-red: #c8202a;
    --feature-rust: #b5561f;
    --white: #ffffff;
  }
  * { box-sizing: border-box; margin: 0; padding: 0; }
  html, body { width: 1200px; height: 900px; overflow: hidden; background: var(--stage); }
  body { font-family: "PT Sans", Arial, sans-serif; color: var(--text); position: relative; }

  .brochure { position: absolute; left: 20px; top: 40px; width: 1160px; height: 820px; overflow: hidden; }
  .panel { position: absolute; top: 0; height: 820px; width: 387px; }
  .panel--left { left: 0; background: linear-gradient(180deg, var(--white) 0%, var(--white) 45%, var(--cream-light) 100%); }
  .panel--middle { left: 387px; width: 386px; background: var(--red); }
  .panel--right { left: 773px; background: linear-gradient(180deg, var(--cream-light) 0%, var(--cream) 100%); }

  .band-strip {
    position: absolute; left: 0; top: 424px; width: 1160px; height: 40px; z-index: 1;
    background: linear-gradient(180deg, var(--band-orange) 0%, var(--band-orange) 30%, var(--band-blue) 30%, var(--band-blue) 62%, var(--band-green) 62%, var(--band-green) 100%);
  }

  .content { position: absolute; z-index: 2; }

  .section-title { font-weight: 700; color: var(--blue-title); font-size: 21px; line-height: 1.1; margin-bottom: 14px; }
  .body-text { font-size: 12.5px; line-height: 1.45; text-align: justify; margin-bottom: 12px; }

  .left-top { left: 28px; top: 34px; width: 332px; }
  .left-mid { left: 28px; top: 482px; width: 332px; }

  .photo { position: absolute; z-index: 2; }
  .photo-row { display: flex; gap: 8px; }

  .custom { left: 414px; top: 38px; width: 330px; color: var(--white); }
  .custom .section-title { color: var(--white); font-size: 18px; margin-bottom: 6px; }
  .custom .body-text { font-size: 11px; color: var(--white); text-align: left; }

  .photo-grid { position: absolute; z-index: 2; left: 420px; top: 120px; width: 310px; display: grid; grid-template-columns: 1fr 1fr; gap: 6px; }
  .photo-grid .tile { height: 80px; }

  .contact { left: 400px; top: 540px; width: 360px; color: var(--white); font-size: 14px; line-height: 1.55; }
  .contact h3 { text-align: center; font-size: 15px; margin-bottom: 10px; }
  .contact .indent { padding-left: 58px; }

  .brand { left: 810px; top: 50px; width: 320px; display: flex; align-items: center; gap: 12px; }
  .brand-mark { width: 56px; height: 56px; background: var(--red); flex: none; }
  .brand-name { font-weight: 700; font-size: 24px; line-height: 1.15; color: #1d1d1d; letter-spacing: 1px; }

  .tagline {
    left: 820px; top: 300px; width: 320px; text-align: center;
    font-family: "Cinzel", Georgia, serif; font-size: 20px; color: var(--red); letter-spacing: 1px;
    transform: rotate(-30deg); transform-origin: center;
  }

  .features { left: 810px; top: 520px; width: 320px; display: grid; grid-template-columns: 1fr 1fr; gap: 22px 16px; }
  .feature { font-family: "Cinzel", Georgia, serif; font-size: 15px; font-weight: 700; line-height: 1.25; text-align: center; }
  .feature--multi { color: var(--feature-beige); }
  .feature--custom { color: var(--feature-yellow); }
  .feature--max { color: var(--feature-red); }
  .feature--oneday { color: var(--feature-rust); }

  .badges { left: 820px; top: 740px; display: flex; gap: 26px; align-items: center; }
  .badge { width: 44px; height: 36px; background: #3a3a3a; border-radius: 4px; }
  .badge--round { width: 38px; height: 38px; border-radius: 50%; background: #4f8f2a; }
  .badge--green { background: #6aa12b; }
  .badge--red { background: var(--red); }
</style>
</head>
<body>
<main class="brochure" aria-label="Brambleway TRUEpath Tours tri-fold brochure, front side">
  <div class="panel panel--left"></div>
  <div class="panel panel--middle"></div>
  <div class="panel panel--right"></div>

  <div class="band-strip" role="img" aria-label="Decorative flowing ribbon band in orange, blue and green across all three panels"></div>

  <section class="content left-top">
    <h2 class="section-title">Phillip Island</h2>
    <p class="body-text">See penguins, koalas, birdlife and experience history on our one day wildlife tour of Phillip Island which includes an evening at the iconic penguin parade.</p>
    <p class="body-text">For the ultimate wildlife tour, our 2 day tour of Phillip Island will ensure you experience nature at its best. See koalas, little penguins, wallabies and choose from options to see fur seals, catch your own trout or take a helicopter ride to French Island. Choose from a private tour or small group tour with a maximum of 6 in luxury 4WD vehicles.</p>
  </section>
  <div class="photo photo-row" style="left:28px; top:292px;">
    <div role="img" aria-label="Photo of rocky coastline at Phillip Island" style="width:178px;height:118px;background:linear-gradient(180deg,#6fa6c8 0%,#3f7f9a 45%,#8a6a4a 100%);"></div>
    <div role="img" aria-label="Photo of penguins on the beach at sunset" style="width:146px;height:118px;background:linear-gradient(180deg,#d99a4a 0%,#8a5a2a 60%,#3a2a1a 100%);"></div>
  </div>

  <section class="content left-mid">
    <h2 class="section-title">Indigenous Tours</h2>
    <p class="body-text">Enjoy an amazing journey of discovery on this 4 day Indigenous tour where you will explore Victoria's Indigenous history with a range of local Indigenous Groups. You will see spectacular coastal scenery along the Great Ocean Road and experience amazing views in the rugged and beautiful Grampians / Gariwerd region.</p>
    <p class="body-text">Choose from a private tour or small group tour with a maximum of 6 in luxury 4WD vehicles.</p>
  </section>
  <div class="photo photo-row" style="left:28px; top:700px;">
    <div role="img" aria-label="Photo of misty mountain range in the Grampians" style="width:160px;height:96px;background:linear-gradient(180deg,#c9ccc8 0%,#8a8f86 55%,#4f5a45 100%);"></div>
    <div role="img" aria-label="Photo of ancient rock art on sandstone" style="width:164px;height:96px;background:linear-gradient(135deg,#c89a5a 0%,#a8743a 60%,#7a5028 100%);"></div>
  </div>

  <section class="content custom">
    <h2 class="section-title">Custom Tours</h2>
    <p class="body-text">Here at Brambleway TRUEpath Tours we say that "its all about YOU", that's why we'll customise tours around you and your interests.</p>
  </section>
  <div class="photo-grid">
    <div class="tile" role="img" aria-label="Photo of bracket fungi on a tree trunk" style="background:linear-gradient(135deg,#d8c8a8,#6a5a40);"></div>
    <div class="tile" role="img" aria-label="Photo of green tree fern fronds" style="background:linear-gradient(135deg,#6a9a3a,#2a4a1a);"></div>
    <div class="tile" role="img" aria-label="Photo of gnarled driftwood in the bush" style="background:linear-gradient(135deg,#9a9a8a,#5a5a4a);"></div>
    <div class="tile" role="img" aria-label="Photo of a peacock on a lawn" style="background:linear-gradient(135deg,#8a9a7a,#3a5a6a);"></div>
    <div class="tile" role="img" aria-label="Photo of a colourful parrot on leaf litter" style="background:linear-gradient(135deg,#8a6a4a,#b8302a);"></div>
    <div class="tile" role="img" aria-label="Photo of a sunset over the sea" style="background:linear-gradient(180deg,#e0903a,#5a3a2a);"></div>
  </div>

  <section class="content contact">
    <h3>Contact details</h3>
    <p>Website: <strong>www.bramblewaytours.com.au</strong></p>
    <p>E: <strong>enquiries@bramblewaytours.com.au</strong></p>
    <p>T: <strong>+61 3 9512 0744</strong> F: <strong>+61 3 9512 0748</strong></p>
    <p>Darren M: <strong>0427 615 208 International</strong></p>
    <p class="indent"><strong>+61 427 615 208</strong></p>
    <p>PO Box 287, Wattlebrook Vic 3099</p>
  </section>

  <div class="content brand">
    <span class="brand-mark" aria-hidden="true"></span>
    <span class="brand-name">Brambleway TRUEpath Tours</span>
  </div>

  <p class="content tagline">« Where its all about you »</p>

  <ul class="content features" style="list-style:none;">
    <li class="feature feature--multi">Multi Day<br>Tours</li>
    <li class="feature feature--max">Maximum<br>6 Guests</li>
    <li class="feature feature--oneday">One Day<br>Tours</li>
    <li class="feature feature--custom">Custom<br>Tours</li>
  </ul>

  <div class="content badges" aria-label="Accreditation badges">
    <span class="badge"></span>
    <span class="badge badge--round"></span>
    <span class="badge badge--green"></span>
    <span class="badge badge--red"></span>
  </div>
</main>
</body>
</html>
```